Luxury Courtside Grove/academy - Webdesign

We want to develop a cutting edge website for a luxury tennis academy. Academy is based in Russia and includes all the necessary amenities for comfortable stay: apartments, spa, tennis courts, training facilities, etc.
We would like to see a clean, simple and modern design (with implementation of all the current trends in web design, although our project has to be distinct and unique).
Color scheme: we would like to see colors present in our logos and all the current associated with tennis. We are open to your ideas and creativity on this front.
The final design should communicate simplicity, be user friendly and convey premium feel.
We woud like to see unique ideas in the design, unconventional techniques, etc.
We don't want standard template design!
Updates
We want to mention that this Tennis Academy has a light focus on nature, as the new material we have uploaded illustrates.
Additional comment to everyone!
We couldn't upload this file to the system: it is too big.
Thank you everyone for your submissions!
Industry/Entity Type
Training
Requirements
Must have
- We would like to see the designs for the following pages:
Home Page:
- Slideshow
- Short description and all the standard stuff
About Us:
- Description with some images
Services:
- Simple description of all of the provided services and possibility to book all of them on the website
! Important ! Develop small system for booking of the days of stay and registration for the courses
Booking and registration !
News:
- Creative layout to display recent news of the academy
Coaches:
- Image and short description of our staff.
Club / Gallery:
- Images and descriptions of the amenities in the territory.
We want a unique display of images: not just lines and rows filled with images
- One idea: an interactive map that displays images and description on mouseover or click on the object on the map (but again, we are open to all your ideas)
Contacts:
- Contact form, contacts, etc.
Sport Store:
- Basic layout for the goods and services provided by the sports store located in the academy
Prices:
- Price lists and ranges with a button leading to registration and booking
For pages like About Us and Services, it would be enough to develop one unified layout for all of them.

```html
<!DOCTYPE html>
<html lang="en">
<head>
<meta charset="utf-8">
<title>Courtside Grove – Tennis Academy</title>
<link rel="stylesheet" href="https://fonts.googleapis.com/css2?family=Ubuntu:ital,wght@0,400;0,500;0,700;1,400;1,700&display=swap">
<style>
:root{
  --night:#050d24;
  --deep:#0a1f4e;
  --panel:#0b2a6e;
  --panel-dark:#061b4f;
  --blue:#1a8fe0;
  --blue-light:#3bb2f5;
  --blue-dark:#0a57b3;
  --green:#7ad11b;
  --green-light:#9fe635;
  --green-dark:#4c9e0c;
  --white:#ffffff;
  --text:#444b55;
  --muted:#8b95a6;
  --link:#4fc4ff;
}
*{box-sizing:border-box;margin:0;padding:0}
html,body{width:1040px;height:1200px;overflow:hidden}
body{
  position:relative;
  font-family:"Ubuntu",Tahoma,sans-serif;
  background:
    radial-gradient(ellipse 520px 300px at 620px 60px, #1a56b8 0%, #0d2f78 45%, transparent 80%),
    radial-gradient(ellipse 420px 380px at 760px 330px, #1c5ec4 0%, #0b2f7a 50%, transparent 85%),
    var(--night);
  color:var(--white);
}
.abs{position:absolute}

/* header */
.brand{left:102px;top:20px;display:flex;align-items:center;gap:8px}
.brand-name{font-size:32px;font-weight:700;color:var(--green);letter-spacing:-.5px}
.brand-dot{width:26px;height:26px;border-radius:50%;background:var(--green-light)}
.follow{left:700px;top:64px;display:flex;align-items:center;gap:6px;font-size:10px;color:#e6eefc}
.follow span.icon{width:16px;height:16px;border-radius:3px;display:inline-block}
.follow .i1{background:#2a9be3}.follow .i2{background:#d63ea0}.follow .i3{background:#2f5cbf}

.nav{left:100px;top:87px;width:826px;height:28px;display:flex;border-radius:8px 8px 0 0;overflow:hidden;
  background:linear-gradient(#3bb2f5,#1080d8 55%,#0a62c0)}
.nav a{display:flex;align-items:center;justify-content:center;font-size:11.5px;color:#fff;text-decoration:none;
  border-right:1px solid rgba(0,40,110,.55);font-weight:500}
.nav a.shop{background:linear-gradient(#a6ec3c,#6cc414 60%,#4fa30a);color:#0b2a10;border-right:1px solid #3b8a0a}
.nav a:last-child{border-right:0}

/* hero */
.hero{left:102px;top:124px;width:825px;height:280px;border:2px solid #fff}
.player{left:650px;top:-4px;width:150px;height:300px;border-radius:70px 70px 40px 40px;
  background:radial-gradient(ellipse at 50% 35%, rgba(240,240,240,.55), rgba(60,140,210,.15) 70%, transparent)}
.slide{left:13px;top:18px;width:525px;height:249px;background:#fff;padding:4px}
.slide-img{width:100%;height:100%;background:linear-gradient(120deg,#e8a94a 0%,#d9b79a 30%,#f1ddcb 55%,#e9c7a9 80%,#c48b62 100%)}
.arrow{top:108px;width:30px;height:36px}
.arrow.prev{left:10px}.arrow.next{right:10px}
.caption{left:44px;top:184px;width:476px}
.caption-title{height:32px;border-radius:8px 0 0 0;background:linear-gradient(#2fa6f0,#0c7ad4);
  font-size:16px;padding:6px 16px;letter-spacing:.2px}
.caption-sub{height:24px;background:#063e96;display:flex;justify-content:space-between;align-items:center;padding:0 10px 0 16px;font-size:10px}
.caption-sub .more{color:#3fb0f5}

/* amenities */
.tab{left:100px;top:435px;width:112px;height:24px;border-radius:8px 8px 0 0;background:linear-gradient(#2fa6f0,#0a62c0);
  font-size:11px;font-weight:700;font-style:italic;padding:5px 0 0 20px}
.amen{left:102px;top:451px;width:585px;height:119px;background:#fff;border-top:7px solid var(--blue-dark)}
.amen-btn{top:42px;width:28px;height:28px;background:linear-gradient(var(--green-light),var(--green-dark))}
.thumb{top:15px;width:102px;text-align:center;color:#222;font-size:10px}
.thumb .ph{height:71px;border:1px solid #6b5a3b;margin-bottom:10px}

/* content boxes */
.card{top:586px;height:368px;background:#fff;border-radius:0 0 10px 10px;color:var(--text)}
.card-head{height:28px;background:linear-gradient(#9ce93b,#63c011 60%,#4ba00b);color:#fff;font-size:15.5px;
  display:flex;align-items:center;gap:8px;padding-left:9px}
.card-head i{width:9px;height:9px;background:#fff;display:inline-block;border-radius:1px;position:relative}
.card-head i:after{content:"";position:absolute;left:3px;top:2px;border-left:4px solid var(--green-dark);border-top:2.5px solid transparent;border-bottom:2.5px solid transparent}
.btn{position:absolute;height:17px;padding:0 7px;border-radius:2px;background:linear-gradient(#3ab6f7,#0b6fd0);color:#fff;font-size:9.5px;
  display:flex;align-items:center;font-weight:700}
.body-text{font-size:9.6px;line-height:13.9px;text-align:justify;color:#6a707a}

/* sidebar */
.side{left:732px;width:194px;background:var(--panel-dark)}
.side-head{height:42px;background:linear-gradient(#31a8f1,#0b66c8);display:flex;align-items:center;gap:10px;padding-left:10px;font-size:16px;font-weight:500}
.ql{margin:19px 10px 0;list-style:none}
.ql li{height:23px;display:flex;align-items:center;gap:12px;padding-left:10px;font-size:9.6px;font-weight:500}
.ql li:nth-child(odd){background:#0b45a6}
.ql li:nth-child(even){background:#071c4e}
.ql li:before{content:"»";color:#9fd4ff;font-size:11px}
.upd{padding:14px 11px 0 11px}
.upd .date{font-size:8.6px}.upd .date b{color:var(--green);font-weight:400}
.upd h4{font-size:11px;font-weight:400;color:var(--link);margin:3px 0 9px}
.upd p{font-size:9.6px;line-height:12.5px;text-align:justify}
.upd hr{border:0;border-top:1px dashed var(--green-dark);margin:12px 0 15px}

/* footer */
.f-title{font-size:20px;display:flex;align-items:center;gap:8px}
.f-title em{font-style:normal;color:var(--green)}
.f-divider{top:980px;width:1px;height:135px;background:#1b2640}
.phone{left:126px;top:1040px;font-size:25px;color:#8fd0ff;text-shadow:0 0 6px #2f7fe0;letter-spacing:.5px}
.mail{left:132px;top:1079px;font-size:14px;color:#b9f06a}
.soc{top:1056px;width:36px;text-align:center;font-size:6.5px;font-weight:700;color:#fff}
.soc span{display:block;width:26px;height:26px;margin:0 auto 4px;border-radius:3px}
.nl-text{left:681px;top:1033px;width:240px;font-size:9.6px;font-style:italic;line-height:12px}
.nl-input{left:676px;top:1068px;width:236px;height:26px;border-radius:8px;background:linear-gradient(#e9edf3,#9aa3ae);
  color:#0e2e66;font-size:9.6px;padding:7px 12px}
.nl-btn{left:857px;top:1111px;width:72px;height:27px;border-radius:10px;border:2px solid #fff;background:linear-gradient(#93e23a,#4aa00c);
  font-size:10px;display:flex;align-items:center;justify-content:center}
.copy{left:0;top:1146px;width:1040px;text-align:center;font-size:10.4px;color:#e6eefc;letter-spacing:.2px}
.terms{left:0;top:1166px;width:1040px;text-align:center;font-size:9.6px;color:#8b95a6;letter-spacing:.4px}
</style>
</head>
<body>

<header>
  <div class="abs brand"><span class="brand-name">Courtside Grove</span><span class="brand-dot"></span></div>
  <div class="abs follow">FOLLOW US ON :
    <span class="icon i1" aria-label="Chirper"></span><span class="icon i2" aria-label="Snapbox"></span><span class="icon i3" aria-label="Faceline"></span>
  </div>
  <nav class="abs nav">
    <a style="width:65px">ABOUT</a><a style="width:81px">SERVICES</a><a style="width:124px">REGISTRATIONS</a>
    <a style="width:61px">NEWS</a><a style="width:83px">COACHES</a><a style="width:119px">CLUB/GALLERY</a>
    <a style="width:102px">CONTACTS</a><a class="shop" style="width:108px">ONLINE STORE</a><a class="shop" style="width:83px">PRICES</a>
  </nav>
</header>

<section class="abs hero">
  <div class="abs player" role="img" aria-label="Tennis player mid-serve in white kit over a glowing planet"></div>
  <div class="abs slide">
    <div class="slide-img" role="img" aria-label="Spa guest relaxing with flowers, slideshow image"></div>
    <svg class="abs arrow prev" viewBox="0 0 30 36"><path d="M22 2 L6 18 L22 34" fill="none" stroke="#3f86d6" stroke-width="6"/></svg>
    <svg class="abs arrow next" viewBox="0 0 30 36"><path d="M8 2 L24 18 L8 34" fill="none" stroke="#3f86d6" stroke-width="6"/></svg>
    <div class="abs caption">
      <div class="caption-title">THIS SPACE IS FOR SLIDESHOW</div>
      <div class="caption-sub"><span>Two Arrows on image - to rorate slideshow left to right &amp; right to left</span><span class="more">READ MORE »</span></div>
    </div>
  </div>
</section>

<section>
  <div class="abs tab">AMENITIES</div>
  <div class="abs amen">
    <svg class="abs amen-btn" style="left:8px" viewBox="0 0 28 28"><path d="M15 8 L9 14 L15 20 M21 8 L15 14 L21 20" fill="none" stroke="#fff" stroke-width="2.5"/></svg>
    <div class="abs thumb" style="left:51px"><div class="ph" role="img" aria-label="Apartment interior" style="background:linear-gradient(#a6743f,#6b3f1c)"></div>Apartments</div>
    <div class="abs thumb" style="left:175px"><div class="ph" role="img" aria-label="Hot stone spa treatment" style="background:linear-gradient(#e9c8ad,#8a5a3f);border-color:#2c4a8a"></div>Spa</div>
    <div class="abs thumb" style="left:302px"><div class="ph" role="img" aria-label="Tennis court with balls" style="background:linear-gradient(#7fa886,#3e6b4e);border-color:#2c4a8a"></div>Tennis Courts</div>
    <div class="abs thumb" style="left:428px"><div class="ph" role="img" aria-label="Coach training a young player" style="background:linear-gradient(#cfe3c0,#7fa56a);border-color:#2c4a8a"></div>Training Facilities</div>
    <svg class="abs amen-btn" style="left:547px" viewBox="0 0 28 28"><path d="M7 8 L13 14 L7 20 M13 8 L19 14 L13 20" fill="none" stroke="#fff" stroke-width="2.5"/></svg>
  </div>
</section>

<section class="abs card" style="left:102px;width:285px">
  <div class="card-head" style="margin:8px 5px 0"><i></i>Welcome to Courtside Grove</div>
  <div role="img" aria-label="Outdoor tennis court" style="margin:10px 5px 0;height:87px;border:3px solid #c9463e;background:linear-gradient(#556e48 0%,#4e8d62 30%,#3d9a6a 60%,#b94238 100%)"></div>
  <div style="margin:7px 8px 0;font-size:13px;color:#222">Lorem ipsum dolor sit amet</div>
  <p class="body-text" style="margin:8px 8px 0">consectetuer adipiscing elit, sed diam nonummy nibh euismod tincidunt ut laoreet dolore magna aliquam erat volutpat. consectetuer adipiscing elit, sed diam nonummy nibh euismod tincidunt ut laoreet dolore magna aliquam erat volutpat. consectetuer adipiscing elit, sed diam nonummy nibh euismod tincidunt ut laoreet dolore magna aliquam erat volutpat. consectetuer adipiscing elit, sed diam nonummy nibh euismod tincidunt ut laoreet dolore magna aliquam erat volutpat.</p>
  <span class="btn" style="left:213px;top:341px">Read more</span>
</section>

<section class="abs card" style="left:405px;width:284px">
  <div class="card-head" style="margin:8px 8px 0 9px"><i></i>Video of the Day</div>
  <div style="margin:10px 7px 0 11px;height:148px;background:#000;position:relative">
    <svg class="abs" style="left:103px;top:45px" width="56" height="56" viewBox="0 0 56 56"><circle cx="28" cy="28" r="26" fill="#5a5a5a" stroke="#8a8a8a" stroke-width="2"/><path d="M22 17 L39 28 L22 39Z" fill="#fff"/></svg>
  </div>
  <div style="margin:0 7px 0 11px;height:16px;background:linear-gradient(#f4f4f4,#cfd3d8);position:relative">
    <span class="abs" style="left:3px;top:2px;width:12px;height:12px;border-radius:50%;background:#666"></span>
    <span class="abs" style="left:20px;top:7px;width:132px;height:2px;background:#4aa3e6"></span>
  </div>
  <div class="card-head" style="margin:12px 8px 0 9px"><i></i>Our Coach</div>
  <div role="img" aria-label="Portrait of the head coach" style="position:absolute;left:12px;top:258px;width:73px;height:96px;border:2px solid #2b6b4a;background:linear-gradient(#3c6fa0,#d8b896 55%,#8a8f96)"></div>
  <p class="body-text" style="position:absolute;left:93px;top:256px;width:185px">consectetuer adipiscing elit, sed diam nonummy nibh euismod tincidunt ut laoreet dolore magna aliquam erat volutpat. consectetuer adipiscing elit, sed diam nonummy nibh euismod con- sectetuer ..</p>
  <span class="btn" style="left:211px;top:342px">Read more</span>
</section>

<aside class="abs side" style="top:436px;height:211px">
  <div class="side-head"><svg width="26" height="24" viewBox="0 0 26 24"><path d="M2 2 L12 12 L2 22 M12 2 L22 12 L12 22" fill="none" stroke="#fff" stroke-width="4"/></svg>QUICK LINKS</div>
  <ul class="ql"><li>APARTMENTS</li><li>TENNIS COURTS</li><li>SPA</li><li>TRAINING FACILITIES</li><li>BOOKINGS</li></ul>
  <span class="btn" style="left:116px;top:185px">Read more</span>
</aside>

<aside class="abs side" style="top:663px;height:291px">
  <div class="side-head"><svg width="26" height="24" viewBox="0 0 26 24"><path d="M2 2 L12 12 L2 22 M12 2 L22 12 L12 22" fill="none" stroke="#fff" stroke-width="4"/></svg>UPDATES</div>
  <div class="upd">
    <div class="date"><b>Tuesday</b>, 09 June 2009</div>
    <h4>Lorem ipsum dolor sit amet</h4>
    <p>We can rotate the news from top to down or down to top by maquee, sed diam nonummy nibh euismod tincid- unt ut laoreet dolore magna.</p>
    <hr>
    <div class="date"><b>Tuesday</b>, 09 June 2009</div>
    <h4>Lorem ipsum dolor sit amet</h4>
    <p>consectetuer adipiscing elit, sed diam nonummy nibh euismod tincid- unt ut laoreet dolore magna aliquam erat volutpat.</p>
  </div>
  <span class="btn" style="left:116px;top:267px">Read more</span>
</aside>

<footer>
  <div class="abs f-title" style="left:102px;top:990px">
    <svg width="32" height="32" viewBox="0 0 32 32"><rect width="32" height="32" rx="4" fill="#6cc414"/><text x="16" y="24" text-anchor="middle" font-family="Ubuntu,sans-serif" font-size="22" font-weight="700" fill="#fff">?</text></svg>
    Need Help <em>Now?</em></div>
  <div class="abs phone">8000-555-210</div>
  <div class="abs mail">mail@courtsidegrove.com</div>
  <div class="abs f-divider" style="left:329px"></div>

  <div class="abs f-title" style="left:367px;top:992px">
    <svg width="44" height="28" viewBox="0 0 44 28"><circle cx="22" cy="14" r="12" fill="#2a8be0"/></svg>
    Follow <em>Us</em></div>
  <div class="abs soc" style="left:403px"><span style="background:#4fbde8"></span>CHIRPER</div>
  <div class="abs soc" style="left:443px"><span style="background:#3560b8"></span>FACELINE</div>
  <div class="abs soc" style="left:484px"><span style="background:#3f8a2a"></span>PODCAST</div>
  <div class="abs soc" style="left:525px"><span style="background:#dfe3e8"></span>NEWSLETTER</div>
  <div class="abs soc" style="left:566px"><span style="background:#f07a1e"></span>RSS</div>
  <div class="abs f-divider" style="left:635px"></div>

  <div class="abs f-title" style="left:675px;top:990px">
    <svg width="32" height="30" viewBox="0 0 32 30"><rect x="2" y="6" width="26" height="20" rx="2" fill="#dfe8f2"/><path d="M2 6 L15 17 L28 6" fill="none" stroke="#3a7fd0" stroke-width="2"/></svg>
    Subscribe to <em>Newsletter</em></div>
  <p class="abs nl-text">Lorem Ipsum is simply dummy text of the printing and typesetting</p>
  <div class="abs nl-input">Enter E Mail ID</div>
  <div class="abs nl-btn">Subscribe</div>

  <div class="abs copy">© 2012 Courtside Grove. All Rights Reserved. The Courtside Grove Name, Logo and Related Marks are Trademarks of Courtside Grove</div>
  <div class="abs terms">Terms and Conditions | F.A.Q's | Login.</div>
</footer>

</body>
</html>
```